business card design - photography

I am a fine art photographer. I would like to approach galleries to exhibit my work and need a business card.

The card should convey creativity and simplicity.
I would like a double sided card.

Some options:
1. An all white card with raised or embossed text or design to create a tactile finish.
2. a white and dark grey design would also work well.
3. Would be great to use my name as part of the design but not essential.
4. My name and title on the front, other details on the back of card.

The final design should be simple, minimal, elegant and innovative.
Being minimal, it will be more about texture, text size and placement.

examples of designs I would prefer provided here:
http://plimvarka.com/ideas/40-quiet-and-refined-card-layouts

I'm also open to other designs that may be unusual and unique.

Love this:
http://www.snapvelo.com/pics/morningverselog/583014927
Updates

I have uploaded a psd file after playing around in photoshop with various fonts.  I like the font (which I downloaded from glyphmorra.com called Arual) but the design probably needs some refining.  I hope this helps.  If you'd like me to change the format of the file, please let me know.

Ilvane

Target Market(s)

Art Gallery owners/administrators and customers.

Industry/Entity Type

Business

Requirements
Must have
• A unique look.

Matte, silky finish or heavy textured stock. Double-sided card.

Front:
my name
photography by

Back:
phone no
email
web address
Nice to have
• Letterpress
embrossed
Clean fonts
Should not have
• Do not use illustrations of cameras or lenses.
No frames around the card edge.

```html
<!DOCTYPE html>
<html lang="en">
<head>
<meta charset="utf-8">
<title>Ilvane Marrow Photography – Business Card</title>
<link rel="stylesheet" href="https://fonts.googleapis.com/css2?family=Montserrat:wght@400&family=Oswald:wght@200;300&display=swap">
<style>
  :root {
    --page: #ffffff;
    --ink: #2f2f2f;
    --card-gray: #bcbdc0;
    --print-light: #e4e4e6;
  }
  * { margin: 0; padding: 0; box-sizing: border-box; }
  html, body { width: 1200px; height: 900px; overflow: hidden; background: var(--page); }
  body { position: relative; font-family: "Montserrat", Arial, sans-serif; color: var(--ink); }

  .spec-note {
    position: absolute;
    text-align: center;
    font-size: 16px;
    line-height: 20.5px;
    white-space: nowrap;
  }
  .spec-note h2 { font-weight: 400; font-size: 25px; line-height: 30px; }
  .spec-front { left: 118px; top: 28px; width: 500px; }
  .spec-back  { left: 591px; top: 28px; width: 500px; }
  .spec-stock { left: 300px; top: 778px; width: 600px; }

  .card {
    position: absolute;
    width: 307px;
    height: 501px;
    background: var(--card-gray);
    color: var(--print-light);
    font-family: "Oswald", "Arial Narrow", sans-serif;
    font-weight: 200;
    text-align: center;
  }
  .card-front { left: 212px; top: 201px; }
  .card-back  { left: 688px; top: 203px; }

  .monogram-name {
    position: absolute;
    left: 0; right: 0; top: 150px;
    font-size: 64px;
    line-height: 74px;
    letter-spacing: 4px;
    font-weight: 300;
  }
  .card-back .monogram-name { top: 130px; }

  .front-signature {
    position: absolute;
    left: 0; right: 0; top: 410px;
    display: flex;
    flex-direction: column;
    align-items: center;
  }
  .front-name {
    font-size: 27px;
    line-height: 32px;
    letter-spacing: 1.5px;
    border-bottom: 1.5px solid var(--print-light);
    padding: 0 1px 1px;
    white-space: nowrap;
  }
  .front-title {
    margin-top: 4px;
    padding-left: 8px;
    font-size: 10px;
    line-height: 12px;
    letter-spacing: 8px;
    font-weight: 300;
  }

  .contact-list {
    position: absolute;
    left: 0; right: 0; top: 394px;
    list-style: none;
    font-size: 14.5px;
    line-height: 21px;
    letter-spacing: 1.2px;
  }
</style>
</head>
<body>

  <section class="spec-note spec-front">
    <h2>Front</h2>
    <p>The “S” and the borders are embossed and<br>printed in Pantone Cool Gray 2M (Solid Matte).<br>Ilvane Marrow photograpy is not embossed, only<br>printer in Pantone Cool Gray 2M (Solid Matte)</p>
  </section>

  <section class="spec-note spec-back">
    <h2>Back</h2>
    <p>The “S” and the borders are debossed.<br>The contact information is printed in<br>Pantne Gray 2M (Solid Matte)</p>
  </section>

  <article class="card card-front">
    <div class="monogram-name">ILVANE<br>MARROW</div>
    <div class="front-signature">
      <div class="front-name">ILVANE MARROW</div>
      <div class="front-title">PHOTOGRAPHY</div>
    </div>
  </article>

  <article class="card card-back">
    <div class="monogram-name">ILVANE<br>MARROW</div>
    <ul class="contact-list">
      <li>ILVANE MARROW PHOTOGRAPHY</li>
      <li>0491 552 087</li>
      <li>ILVANE.M@MAILVERO.COM</li>
      <li>WWW.ILVANEMARROW.COM</li>
    </ul>
  </article>

  <section class="spec-note spec-stock">
    <p>Card background is either printed in Pantone Cool Gray 5M<br>(Solid Matte), or use a paper that is “dolphin gray”. You will<br>have to ask the printer for paper sample. I would recomend<br>using a paper thickness of 230-270 grams, to get the right<br>feel when holding the card</p>
  </section>

</body>
</html>
```